Redesign one screen in a mobile app

I have an app called Toasts and Tallies (available on iOS and Android). This app allows wedding guests to bet on things that happen during a wedding they are attending (think: will the groom cry when the bride walks down the aisle...). The event is set up by someone called the "event leader", typically this is the bride or the groom.

Once event details, bets, and $ values of the bets are entered, the event leader publishes the event and gets to the event detail homescreen, where they can manage their event. The three main things they can do are:

1.) Share the event with other guests to join in the betting.
2.) Edit the event -- add, change, or delete bets.
3.) Add a co-organizer. If you are the bride or the groom, you want someone else managing the event on your wedding day.

I'd like to redesign this page, make it simpler, and *focus attention on sharing the event.* The biggest goal of this page is getting event leaders to share the event. We want them to invite as many wedding guests as possible.

To that end, I would like to also introducing "sharing tiers" to entice more sharing and I'd like this to be something event leaders can easily see once they hit the event homescreen. Tiers are as follows:
Share with 1 guest, unlock co-organizer feature.
Share with 5 guests, unlock physical placard with custom QR code.
Share with 10 guests, we split our proceeds with the bride and groom.
Share with 20 guests, you are entered into $250 monthly raffle.

Some additional requests:
+ Please do not use current fonts. We want new fonts that are cleaner.
+ Share options should stay the same (copy, share, QR code)
+ Need to keep "help" question mark on page as well.
+ Maintain colors generally. Red button color must be kept as is because it's used throughout app. Slight variations to other colors OK.
+ Navigation at bottom must remain.
+ Feel free to add moving elements as well, like gifs.
+ Final design delivered in Figma.
Updates

Submissions need to be app designs. Not webpages.

The current actions shown on the page need to remain - share event, edit event, add a Co-Organizer. But the goal of the design is to make the page simpler, not more complicated.

Sharing tiers can be a separate screen, linked from the event home screen. This information does not need to live on the same page!

Target Market(s)

25-40 year olds

Industry/Entity Type

Mobile Apps - Betting

Font styles to use
Sans Serif
Other font styles liked:
• I like poppins, but open to other options.

Requirements
Must have
• Fun design that focuses on sharing an event. Design delievered in Figma.

```html
<!DOCTYPE html>
<html lang="en">
<head>
<meta charset="utf-8">
<title>Toasts and Tallies – Event Details</title>
<link href="https://fonts.googleapis.com/css2?family=Roboto:wght@400;500;700&display=swap" rel="stylesheet">
<style>
:root{
  --red:#e25d4f;
  --red-soft:#fdecea;
  --ink:#1f1f24;
  --muted:#6e6e76;
  --line:#e6e6ea;
  --bg:#f6e3dc;
  --white:#ffffff;
  --green-bg:#f2f6e1; --green:#93ad10;
  --blue-bg:#e8f5f8; --blue:#19a2c2;
  --purple-bg:#f5ebfb; --purple:#a333cf;
  --pink-bg:#fcebea; --pink:#e0584d;
}
*{box-sizing:border-box;margin:0;padding:0}
html,body{width:1200px;height:900px;overflow:hidden}
body{background:var(--bg);font-family:"Roboto",sans-serif;color:var(--ink);position:relative}
.screen{position:absolute;top:44px;width:375px;height:812px;background:var(--white);border-radius:40px;overflow:hidden;box-shadow:0 20px 50px rgba(160,70,50,.18)}
.screen--overview{left:190px}
.screen--scrolled{left:635px}
.hero{position:absolute;left:0;top:0;width:100%;height:190px;
  background:linear-gradient(180deg,#6f5a86 0%,#b07aa0 28%,#7fb7c4 48%,#4a8f8c 58%,#5c7a3a 72%,#9a6a4e 100%)}
.status{position:absolute;top:14px;left:32px;right:28px;display:flex;justify-content:space-between;color:var(--white);font-size:15px;font-weight:500}
.status svg{display:block}
.topbar{position:absolute;top:54px;left:22px;right:22px;height:30px;display:flex;align-items:center;color:var(--white)}
.topbar h1{font-size:16px;font-weight:500;margin-left:14px;flex:1}
.round-btn{width:30px;height:30px;border-radius:50%;background:var(--red);display:flex;align-items:center;justify-content:center;margin-left:14px}
.sheet{position:absolute;left:0;right:0;bottom:0;background:var(--white);border-radius:16px 16px 0 0;overflow:hidden}
.abs{position:absolute}
.bets-badge{left:22px;top:22px;width:68px;height:76px;border-radius:4px;background:var(--red);color:var(--white);font-size:13px;display:flex;flex-direction:column;align-items:center;justify-content:center;gap:12px}
.event-title{left:110px;top:20px;width:245px;font-size:17px;line-height:22px;font-weight:400}
.meta{left:110px;top:80px;display:flex;gap:16px;font-size:13px;color:var(--ink)}
.meta span{display:flex;align-items:center;gap:5px}
.invite{left:22px;width:331px;height:70px;border-radius:8px;background:var(--red-soft);display:flex;align-items:center;padding:0 22px}
.invite .avatar-btn{width:38px;height:38px;border-radius:50%;background:var(--red);display:flex;align-items:center;justify-content:center;flex:none}
.invite .txt{margin-left:14px;flex:1}
.invite strong{display:block;font-size:13.5px;font-weight:500}
.invite strong em{font-style:normal;color:var(--red)}
.invite small{display:block;font-size:11px;color:var(--muted);margin-top:4px}
.tiers{left:22px;width:331px;display:grid;grid-template-columns:1fr 1fr;gap:13px 13px}
.tier{height:121px;border-radius:6px;padding:22px 22px 0}
.tier b{display:block;font-size:11.5px;font-weight:500}
.tier p{font-size:11.5px;line-height:17.5px;color:var(--muted);margin-top:10px}
.tier--green{background:var(--green-bg)}.tier--green b{color:var(--green)}
.tier--blue{background:var(--blue-bg)}.tier--blue b{color:var(--blue)}
.tier--purple{background:var(--purple-bg)}.tier--purple b{color:var(--purple)}
.tier--pink{background:var(--pink-bg)}.tier--pink b{color:var(--pink)}
.org-title{left:22px;font-size:13.5px;font-weight:500}
.org-add{right:22px;width:31px;height:31px;border-radius:50%;background:var(--red);display:flex;align-items:center;justify-content:center}
.org-desc{left:22px;width:280px;font-size:11.5px;line-height:17.5px;color:var(--muted)}
.people{left:22px;right:22px;display:flex;align-items:flex-start}
.person{width:94px;text-align:center;font-size:11.5px;color:var(--muted)}
.person .photo{width:48px;height:48px;border-radius:50%;margin:0 auto 14px;background:linear-gradient(135deg,#c9a58c,#6b4a3a)}
.more{margin-left:auto;width:47px;height:74px;border-radius:24px;background:var(--red-soft);color:var(--red);font-size:11.5px;display:flex;align-items:center;justify-content:center}
.share-bar{position:absolute;left:0;right:0;height:78px;background:var(--red);display:flex;justify-content:space-around;align-items:center;padding:0 28px;color:var(--white);font-size:11.5px;letter-spacing:.2px}
.share-bar div{display:flex;flex-direction:column;align-items:center;gap:14px;width:90px}
.tabbar{position:absolute;left:0;right:0;bottom:0;height:68px;background:var(--white);display:flex;justify-content:space-around;align-items:center;padding:0 30px}
.tab-home{width:48px;height:48px;border-radius:50%;background:var(--red);display:flex;align-items:center;justify-content:center}
</style>
</head>
<body>

<!-- Event details, top of page -->
<section class="screen screen--overview">
  <div class="hero" role="img" aria-label="Beach wedding ceremony with a floral arch, chairs and an aisle by the sea"></div>
  <div class="status"><span>9:41</span>
    <svg width="66" height="12" viewBox="0 0 66 12" fill="#fff"><rect x="0" y="8" width="3" height="4"/><rect x="5" y="6" width="3" height="6"/><rect x="10" y="4" width="3" height="8"/><rect x="15" y="2" width="3" height="10"/><path d="M26 4a10 10 0 0 1 14 0l-1.5 1.5a8 8 0 0 0-11 0zM29 7a6 6 0 0 1 8 0l-4 4z"/><rect x="45" y="2" width="20" height="9" rx="2"/></svg>
  </div>
  <header class="topbar">
    <svg width="20" height="16" viewBox="0 0 20 16" fill="none" stroke="#fff" stroke-width="1.8"><path d="M19 8H2M8 2 2 8l6 6"/></svg>
    <h1>Event Details</h1>
    <span class="round-btn"><svg width="14" height="14" viewBox="0 0 14 14" fill="none" stroke="#fff" stroke-width="1.2"><circle cx="7" cy="7" r="6"/><path d="M5.3 5.3a1.8 1.8 0 1 1 2.3 1.7c-.5.2-.6.5-.6 1v.4"/><circle cx="7" cy="10.2" r=".4" fill="#fff"/></svg></span>
    <span class="round-btn"><svg width="14" height="14" viewBox="0 0 14 14" fill="none" stroke="#fff" stroke-width="1.3"><path d="M2 12l.6-3L9.5 2l2.5 2.5L5 11.4z"/></svg></span>
  </header>

  <main class="sheet" style="top:156px">
    <div class="abs bets-badge">
      <svg width="14" height="12" viewBox="0 0 14 12" fill="none" stroke="#fff" stroke-width="1.2"><rect x="1" y="3" width="10" height="8"/><path d="M3 1h10v8"/></svg>
      <span>3 bets</span>
    </div>
    <h2 class="abs event-title">Groom will cry when the bride walks down the aisle.</h2>
    <div class="abs meta">
      <span><svg width="12" height="12" viewBox="0 0 12 12" fill="none" stroke="#8a8a92"><rect x="1" y="2" width="10" height="9"/><path d="M1 5h10M4 1v2M8 1v2"/></svg>Feb 08</span>
      <span><svg width="12" height="12" viewBox="0 0 12 12" fill="none" stroke="#8a8a92"><circle cx="6" cy="6.5" r="4.5"/><path d="M6 4v3h2"/></svg>5:00 pm</span>
      <span><svg width="11" height="13" viewBox="0 0 11 13" fill="none" stroke="#8a8a92"><path d="M5.5 12s4-4 4-7a4 4 0 0 0-8 0c0 3 4 7 4 7z"/><circle cx="5.5" cy="5" r="1.4"/></svg>Misouri</span>
    </div>

    <div class="abs invite" style="top:121px">
      <span class="avatar-btn"><svg width="18" height="16" viewBox="0 0 18 16" fill="none" stroke="#fff" stroke-width="1.4"><circle cx="7" cy="5" r="3.5"/><path d="M1 15c0-3 2.7-5 6-5s6 2 6 5M14 4v5M11.5 6.5h5"/></svg></span>
      <div class="txt"><strong>Invite guest for <em>$2.99</em></strong><small>More guests, better rewards!</small></div>
      <svg width="14" height="14" viewBox="0 0 14 14" fill="none" stroke="#e25d4f"><circle cx="7" cy="7" r="6"/><path d="M7 6v4"/><circle cx="7" cy="4" r=".5" fill="#e25d4f"/></svg>
    </div>

    <div class="abs tiers" style="top:214px">
      <div class="tier tier--green"><b>1 guest</b><p>Unlock co-organizer feature</p></div>
      <div class="tier tier--blue"><b>5 guests</b><p>Unlock physical placard with custom QR code</p></div>
      <div class="tier tier--purple"><b>10 guests</b><p>We split our proceeds with the bride and groom</p></div>
      <div class="tier tier--pink"><b>20 guests</b><p>You are entered into $250 monthly raffle</p></div>
    </div>

    <h3 class="abs org-title" style="top:490px">Event organizers</h3>
    <span class="abs org-add" style="top:494px"><svg width="14" height="14" viewBox="0 0 14 14" stroke="#fff" stroke-width="1.4"><path d="M7 1v12M1 7h12"/></svg></span>
  </main>

  <nav class="share-bar" style="top:669px">
    <div><svg width="14" height="14" viewBox="0 0 14 14" fill="none" stroke="#fff" stroke-width="1.2"><path d="M6 8a3 3 0 0 0 4 0l2-2a2.8 2.8 0 0 0-4-4l-1 1M8 6a3 3 0 0 0-4 0L2 8a2.8 2.8 0 0 0 4 4l1-1"/></svg>COPY LINK</div>
    <div><svg width="14" height="14" viewBox="0 0 14 14" fill="none" stroke="#fff" stroke-width="1.2"><circle cx="11" cy="3" r="2"/><circle cx="3" cy="7" r="2"/><circle cx="11" cy="11" r="2"/><path d="M5 6l4-2M5 8l4 2"/></svg>SHARE</div>
    <div><svg width="14" height="14" viewBox="0 0 14 14" fill="none" stroke="#fff" stroke-width="1.2"><rect x="1" y="1" width="5" height="5"/><rect x="8" y="1" width="5" height="5"/><rect x="1" y="8" width="5" height="5"/><path d="M8 8h2v2H8zM11 11h2v2h-2z"/></svg>QR CODE</div>
  </nav>
  <nav class="tabbar">
    <span class="tab-home"><svg width="22" height="20" viewBox="0 0 22 20" fill="none" stroke="#fff" stroke-width="1.5"><path d="M2 9 11 2l9 7v10H2zM8 19v-6h6v6"/></svg></span>
    <svg width="20" height="16" viewBox="0 0 20 16" fill="none" stroke="#6e6e76" stroke-width="1.3"><rect x="1" y="4" width="15" height="11"/><path d="M4 1h15v11"/></svg>
    <svg width="20" height="18" viewBox="0 0 20 18" fill="none" stroke="#6e6e76" stroke-width="1.3"><path d="M1 17h18M4 17v-6h4v6M8 17V7h4v10M12 17V2h4v15"/></svg>
  </nav>
</section>

<!-- Event details, scrolled to organizers -->
<section class="screen screen--scrolled">
  <div class="hero" role="img" aria-label="Beach wedding ceremony with a floral arch by the sea"></div>
  <div class="status"><span>9:41</span>
    <svg width="66" height="12" viewBox="0 0 66 12" fill="#fff"><rect x="0" y="8" width="3" height="4"/><rect x="5" y="6" width="3" height="6"/><rect x="10" y="4" width="3" height="8"/><rect x="15" y="2" width="3" height="10"/><path d="M26 4a10 10 0 0 1 14 0l-1.5 1.5a8 8 0 0 0-11 0zM29 7a6 6 0 0 1 8 0l-4 4z"/><rect x="45" y="2" width="20" height="9" rx="2"/></svg>
  </div>
  <header class="topbar">
    <svg width="20" height="16" viewBox="0 0 20 16" fill="none" stroke="#fff" stroke-width="1.8"><path d="M19 8H2M8 2 2 8l6 6"/></svg>
    <h1>Event Details</h1>
    <span class="round-btn"><svg width="14" height="14" viewBox="0 0 14 14" fill="none" stroke="#fff" stroke-width="1.2"><circle cx="7" cy="7" r="6"/><path d="M5.3 5.3a1.8 1.8 0 1 1 2.3 1.7c-.5.2-.6.5-.6 1v.4"/><circle cx="7" cy="10.2" r=".4" fill="#fff"/></svg></span>
    <span class="round-btn"><svg width="14" height="14" viewBox="0 0 14 14" fill="none" stroke="#fff" stroke-width="1.3"><path d="M2 12l.6-3L9.5 2l2.5 2.5L5 11.4z"/></svg></span>
  </header>

  <main class="sheet" style="top:106px">
    <div class="abs invite" style="top:-16px">
      <span class="avatar-btn"><svg width="18" height="16" viewBox="0 0 18 16" fill="none" stroke="#fff" stroke-width="1.4"><circle cx="7" cy="5" r="3.5"/><path d="M1 15c0-3 2.7-5 6-5s6 2 6 5M14 4v5M11.5 6.5h5"/></svg></span>
      <div class="txt"><strong>Invite guest for <em>$2.99</em></strong><small>More guests, better rewards!</small></div>
      <svg width="14" height="14" viewBox="0 0 14 14" fill="none" stroke="#e25d4f"><circle cx="7" cy="7" r="6"/><path d="M7 6v4"/><circle cx="7" cy="4" r=".5" fill="#e25d4f"/></svg>
    </div>

    <div class="abs tiers" style="top:78px">
      <div class="tier tier--green"><b>1 guest</b><p>Unlock co-organizer feature</p></div>
      <div class="tier tier--blue"><b>5 guests</b><p>Unlock physical placard with custom QR code</p></div>
      <div class="tier tier--purple"><b>10 guests</b><p>We split our proceeds with the bride and groom</p></div>
      <div class="tier tier--pink"><b>20 guests</b><p>You are entered into $250 monthly raffle</p></div>
    </div>

    <h3 class="abs org-title" style="top:358px">Event organizers</h3>
    <span class="abs org-add" style="top:357px"><svg width="14" height="14" viewBox="0 0 14 14" stroke="#fff" stroke-width="1.4"><path d="M7 1v12M1 7h12"/></svg></span>
    <p class="abs org-desc" style="top:380px">If the event was created by a bride or groom, assign a guest as co-organizer to manage and close bets during the wedding weekend. They'll receive a notification to take over!</p>

    <div class="abs people" style="top:466px">
      <div class="person" style="width:54px"><div class="photo" role="img" aria-label="Profile photo of Theo Marsh"></div>Theo Marsh</div>
      <div class="person"><div class="photo" role="img" aria-label="Profile photo of Ian Okafor" style="background:linear-gradient(135deg,#8a7a70,#2a2624)"></div>Ian Okafor</div>
      <div class="person"><div class="photo" role="img" aria-label="Profile photo of Lena Cruz" style="background:linear-gradient(135deg,#e2a88f,#7a3e2e)"></div>Lena Cruz</div>
      <div class="more">+2</div>
    </div>
  </main>

  <nav class="share-bar" style="top:670px">
    <div><svg width="14" height="14" viewBox="0 0 14 14" fill="none" stroke="#fff" stroke-width="1.2"><path d="M6 8a3 3 0 0 0 4 0l2-2a2.8 2.8 0 0 0-4-4l-1 1M8 6a3 3 0 0 0-4 0L2 8a2.8 2.8 0 0 0 4 4l1-1"/></svg>COPY LINK</div>
    <div><svg width="14" height="14" viewBox="0 0 14 14" fill="none" stroke="#fff" stroke-width="1.2"><circle cx="11" cy="3" r="2"/><circle cx="3" cy="7" r="2"/><circle cx="11" cy="11" r="2"/><path d="M5 6l4-2M5 8l4 2"/></svg>SHARE</div>
    <div><svg width="14" height="14" viewBox="0 0 14 14" fill="none" stroke="#fff" stroke-width="1.2"><rect x="1" y="1" width="5" height="5"/><rect x="8" y="1" width="5" height="5"/><rect x="1" y="8" width="5" height="5"/><path d="M8 8h2v2H8zM11 11h2v2h-2z"/></svg>QR CODE</div>
  </nav>
  <nav class="tabbar">
    <span class="tab-home"><svg width="22" height="20" viewBox="0 0 22 20" fill="none" stroke="#fff" stroke-width="1.5"><path d="M2 9 11 2l9 7v10H2zM8 19v-6h6v6"/></svg></span>
    <svg width="20" height="16" viewBox="0 0 20 16" fill="none" stroke="#6e6e76" stroke-width="1.3"><rect x="1" y="4" width="15" height="11"/><path d="M4 1h15v11"/></svg>
    <svg width="20" height="18" viewBox="0 0 20 18" fill="none" stroke="#6e6e76" stroke-width="1.3"><path d="M1 17h18M4 17v-6h4v6M8 17V7h4v10M12 17V2h4v15"/></svg>
  </nav>
</section>

</body>
</html>
```